依頼詳細
「企業ロゴ」が黒と黄色のため、基本的なカラーリングベースは、黒色で黄色のあしらいやワンポイントカラーを入れるイメージを持っております。
デザインイメージは、「未来的」「先進的」などを強く主張したいと思っております。

本件は、Topページのみのテストとして、「コンペ形式」となりますが、
当選された場合には、約10ページほどの下層ページのご依頼も約束させて頂きます。
(予算は10万円前後)
さらに、今後の案件にて、「継続的」に案件を斡旋させて頂きたいと思っておりますので、
末長くお付き合いして頂けると幸いです。
また、当選後は、デザインに利用したファイルやデータを提出して頂きたいです。

```html
<!DOCTYPE html>
<html lang="ja">
<head>
<meta charset="UTF-8">
<title>Outlier | Top</title>
<link rel="stylesheet" href="https://fonts.googleapis.com/css2?family=Montserrat:wght@500;700;800;900&family=Noto+Sans+JP:wght@400;700;900&display=swap">
<style>
:root{
  --black:#0a0a0a;
  --ink:#151515;
  --card:#1e1e1e;
  --yellow:#ffd81a;
  --yellow-2:#ffc21c;
  --orange:#ff9d1b;
  --white:#ffffff;
  --grey:#bdbdbd;
}
*{margin:0;padding:0;box-sizing:border-box}
html,body{width:1200px;height:4860px;overflow:hidden}
body{background:var(--black);font-family:"Noto Sans JP",sans-serif;color:var(--white);position:relative}
a{text-decoration:none}
.abs{position:absolute}

/* header */
.site-header{position:absolute;top:0;left:0;width:1200px;height:70px;display:flex;align-items:center;justify-content:space-between;padding:0 40px;z-index:5}
.logo{display:flex;align-items:center;gap:10px;font-family:"Montserrat",sans-serif;font-weight:800;font-size:24px;color:var(--white)}
.logo-dot{width:12px;height:12px;border-radius:50%;background:var(--yellow)}
.nav{display:flex;align-items:center;gap:46px;font-family:"Montserrat",sans-serif;font-weight:700;font-size:14px;letter-spacing:.08em}
.nav a{color:var(--white)}
.nav .btn-contact{background:var(--yellow);color:var(--black);padding:9px 24px;border-radius:20px;font-size:13px}

/* hero */
.hero-bg{left:0;top:0;width:1200px;height:1340px;background:radial-gradient(ellipse at 55% 45%,#5a5a5a 0%,#2a2a2a 25%,#111 55%,#050505 80%)}
.hero-title{left:200px;top:70px;font-family:"Montserrat",sans-serif;font-weight:900;font-size:112px;line-height:1.15;color:var(--yellow);letter-spacing:-.05em}
.hero-creed{left:800px;top:345px;font-size:26px;font-weight:900;line-height:1.35;color:var(--white)}
.hero-creed span{display:inline-block;background:var(--black);padding:0 4px;margin-bottom:2px}
.hero-side{left:1088px;top:130px;writing-mode:vertical-rl;font-family:"Montserrat",sans-serif;font-size:12px;letter-spacing:.3em;color:var(--white)}

/* about */
.about-label{left:260px;top:650px;font-family:"Montserrat",sans-serif;font-weight:800;font-size:34px;color:var(--yellow);letter-spacing:.06em}
.about-label small{font-family:"Noto Sans JP",sans-serif;font-size:12px;color:var(--white);margin-left:10px;letter-spacing:0}
.about-blob{left:210px;top:700px}
.about-heading{left:470px;top:760px;font-size:42px;font-weight:900;line-height:1.35;color:var(--black)}
.about-text{left:290px;top:960px;width:600px;font-size:15px;line-height:1.9;color:var(--black);font-weight:700}
.pill{display:inline-flex;align-items:center;gap:14px;font-family:"Montserrat",sans-serif;font-weight:700;font-size:14px;padding:12px 34px;border-radius:30px}
.pill-dark{background:var(--ink);color:var(--yellow)}
.pill-yellow{background:var(--yellow);color:var(--black)}
.pill i{display:inline-block;width:26px;height:2px;background:currentColor}
.about-btn{left:420px;top:1110px}

/* services */
.services{left:0;top:1340px;width:1200px;height:1540px;background:linear-gradient(160deg,var(--yellow) 0%,var(--yellow-2) 55%,var(--orange) 100%)}
.sec-title{font-family:"Montserrat",sans-serif;font-weight:900;font-size:58px;letter-spacing:.12em;line-height:1}
.sec-sub{font-size:14px;font-weight:700;margin-top:6px}
.services-title{left:120px;top:1410px;color:var(--black)}
.svc-card{background:var(--card);border-radius:40px;padding:44px 50px;color:var(--white)}
.svc-name{font-family:"Montserrat",sans-serif;font-weight:800;font-size:42px;color:var(--yellow);line-height:1;white-space:nowrap}
.svc-sub{font-size:14px;font-weight:700;margin:8px 0 20px}
.svc-text{width:380px;font-size:15px;line-height:1.9;color:#e8e8e8}
.svc-card .pill{margin-top:26px;padding:10px 28px;font-size:13px}
.card-1{left:140px;top:1520px;width:520px;height:400px}
.card-2{left:580px;top:1980px;width:580px;height:310px;padding:40px 50px}
.card-2 .svc-text{width:470px}
.card-3{left:140px;top:2360px;width:520px;height:340px;padding:40px 50px}

/* works */
.dark-bg{left:0;top:2880px;width:1200px;height:1260px;background:radial-gradient(ellipse at 40% 30%,#3a3a3a 0%,#161616 40%,#060606 75%)}
.works-blob{left:40px;top:3100px}
.works-title{left:80px;top:3165px;color:var(--black)}
.works-title .sec-title,.news-title .sec-title{font-size:44px;letter-spacing:.06em}
.arrows{left:120px;top:3290px;display:flex;gap:40px}
.work-card{top:3150px;width:480px;height:370px;border-radius:32px;overflow:hidden;background:var(--yellow)}
.work-card .ph{height:270px}
.work-meta{display:flex;justify-content:space-between;padding:30px 36px;color:var(--black);font-weight:700;font-size:18px}
.work-1{left:340px}
.work-2{left:860px}

/* news */
.news-blob{left:50px;top:3640px}
.news-title{left:100px;top:3700px;color:var(--black)}
.news-more{left:100px;top:3810px;padding:8px 22px;font-size:12px}
.news-item{top:3870px;width:250px;height:180px;background:var(--yellow);border-radius:24px;display:flex;gap:14px;padding:18px;color:var(--black)}
.news-item .ph{width:90px;height:140px;border-radius:16px;flex:none}
.news-date{font-family:"Montserrat",sans-serif;font-size:12px;font-weight:700}
.news-txt{font-size:13px;font-weight:700;line-height:1.6;margin-top:8px}
.news-1{left:340px}.news-2{left:620px}.news-3{left:900px}.news-4{left:1180px}

/* recruit / contact */
.split{top:4140px;width:600px;height:520px;display:flex;flex-direction:column;align-items:center;justify-content:flex-end;padding-bottom:90px;color:var(--white)}
.recruit{left:0;background:linear-gradient(135deg,#3b2f17,#1b1a16 60%,#2a2414)}
.contact{left:600px;background:linear-gradient(160deg,#1e2636,#3d2e18 60%,#7a4a12)}
.split-title{font-family:"Montserrat",sans-serif;font-weight:900;font-size:72px;color:var(--yellow);letter-spacing:.04em;line-height:1}
.split-sub{font-size:14px;font-weight:700;margin-top:8px}

/* footer */
.site-footer{left:0;top:4660px;width:1200px;height:200px;background:var(--black);display:flex;flex-direction:column;align-items:center;padding-top:30px}
.site-footer .logo{font-size:30px}
.foot-nav{margin-top:26px;gap:70px}
.copy{margin-top:24px;font-family:"Montserrat",sans-serif;font-size:12px;color:var(--grey)}
</style>
</head>
<body>

<header class="site-header">
  <div class="logo"><span class="logo-dot"></span>Outlier</div>
  <nav class="nav">
    <a href="#">SERVICES</a><a href="#">WORKS</a><a href="#">COMPANY</a><a href="#">NEWS</a><a href="#">RECRUIT</a>
    <a href="#" class="btn-contact">CONTACT</a>
  </nav>
</header>

<!-- hero -->
<div class="abs hero-bg" role="img" aria-label="Dark abstract particle burst background"></div>
<h1 class="abs hero-title">BELONGING<br>TO NOTHING,<br>THAT’S<br>THE CREED</h1>
<p class="abs hero-creed"><span>何ものにも</span><br><span>属しはしない</span><br><span>それが信条</span></p>
<p class="abs hero-side">SCROLL DOWN</p>

<!-- about -->
<p class="abs about-label">ABOUT<small>私たちについて</small></p>
<svg class="abs about-blob" width="820" height="500" viewBox="0 0 860 500" preserveAspectRatio="none" aria-hidden="true">
  <defs><linearGradient id="gAbout" x1="0" y1="0" x2="1" y2="1"><stop offset="0" stop-color="#ffe01a"/><stop offset="1" stop-color="#ffa81c"/></linearGradient></defs>
  <path fill="url(#gAbout)" d="M150 70C300 0 520 30 690 45C830 60 880 160 845 270C810 390 700 480 520 458C380 440 250 495 130 452C20 410-10 310 35 210C60 140 80 100 150 70Z"/>
</svg>
<h2 class="abs about-heading">世界の<br>クリエイティブの<br>常識を変える。</h2>
<p class="abs about-text">私たちOutlierは世界を主な活動拠点とするデザイン制作会社です。ホームページ・動画・イラスト・印刷物など幅広いクリエイティブを通じて、企業のブランディングを支援します。</p>
<a class="abs about-btn pill pill-dark">CONTENT<i></i></a>

<!-- services -->
<section class="abs services"></section>
<div class="abs services-title"><p class="sec-title">SERVICES</p><p class="sec-sub">事業内容</p></div>

<div class="abs svc-card card-1">
  <p class="svc-name">Web production</p>
  <p class="svc-sub">WEB制作</p>
  <p class="svc-text">私たちOutlierは世界を主な活動拠点とするデザイン制作会社です。ホームページ・動画・イラストなど幅広く支援します。</p>
  <a class="pill pill-yellow">View more<i></i></a>
</div>
<svg class="abs" style="left:690px;top:1460px" width="470" height="460" viewBox="0 0 420 440" preserveAspectRatio="none" role="img" aria-label="Photo of a futuristic digital globe interface">
  <defs><radialGradient id="gWeb" cx=".5" cy=".45" r=".6"><stop offset="0" stop-color="#e9eef7"/><stop offset=".45" stop-color="#6d7fa6"/><stop offset="1" stop-color="#1a2238"/></radialGradient></defs>
  <path fill="url(#gWeb)" d="M90 40C190-10 330 10 385 90C440 170 410 290 360 360C300 440 170 450 90 390C10 330-15 220 20 140C35 95 55 60 90 40Z"/>
</svg>

<svg class="abs" style="left:120px;top:1940px" width="440" height="370" viewBox="0 0 420 350" preserveAspectRatio="none" role="img" aria-label="Photo of a golden cube structure">
  <defs><radialGradient id="gFree" cx=".5" cy=".45" r=".6"><stop offset="0" stop-color="#f4d9a0"/><stop offset=".4" stop-color="#a67a3a"/><stop offset="1" stop-color="#111"/></radialGradient></defs>
  <path fill="url(#gFree)" d="M60 60C150 0 300 10 370 70C430 125 420 230 370 290C310 350 190 355 100 320C20 290-10 200 10 140C20 105 35 80 60 60Z"/>
</svg>
<div class="abs svc-card card-2">
  <p class="svc-name">Freelance support</p>
  <p class="svc-sub">フリーランス支援</p>
  <p class="svc-text">独立を目指すクリエイターの案件獲得から契約、税務まで一貫してサポートし、自由な働き方を実現します。</p>
  <a class="pill pill-yellow">View more<i></i></a>
</div>

<div class="abs svc-card card-3">
  <p class="svc-name">Event planning</p>
  <p class="svc-sub">イベント企画／運営</p>
  <p class="svc-text">展示会や音楽ライブなど、企画立案から会場設営、当日の運営まで、心に残る体験をつくり上げます。</p>
  <a class="pill pill-yellow">View more<i></i></a>
</div>
<svg class="abs" style="left:680px;top:2290px" width="470" height="400" viewBox="0 0 500 400" preserveAspectRatio="none" role="img" aria-label="Photo of a city street at sunrise">
  <defs><linearGradient id="gEvent" x1="0" y1="0" x2="0" y2="1"><stop offset="0" stop-color="#cfd6de"/><stop offset=".45" stop-color="#f6e3b0"/><stop offset=".6" stop-color="#8a7a64"/><stop offset="1" stop-color="#2b2f38"/></linearGradient></defs>
  <path fill="url(#gEvent)" d="M120 30C230 -5 380 10 450 70C510 125 500 250 450 320C390 400 250 405 150 370C50 335 0 260 10 170C20 100 60 50 120 30Z"/>
</svg>

<!-- works -->
<div class="abs dark-bg" role="img" aria-label="Dark abstract particle background"></div>
<svg class="abs works-blob" width="280" height="270" viewBox="0 0 280 270" aria-hidden="true">
  <path fill="#ffd81a" d="M50 20C120-5 220 5 260 60C295 110 275 200 225 240C170 280 80 270 35 225C-5 185-10 110 10 70C20 45 30 30 50 20Z"/>
</svg>
<div class="abs works-title"><p class="sec-title">WORKS</p><p class="sec-sub">制作実績</p></div>
<div class="abs arrows" aria-hidden="true">
  <svg width="16" height="24" viewBox="0 0 16 24"><path d="M13 2L3 12l10 10" fill="none" stroke="#0a0a0a" stroke-width="3"/></svg>
  <svg width="16" height="24" viewBox="0 0 16 24"><path d="M3 2l10 10L3 22" fill="none" stroke="#0a0a0a" stroke-width="3"/></svg>
</div>
<article class="abs work-card work-1">
  <div class="ph" role="img" aria-label="Photo of a designer working at a monitor" style="background:linear-gradient(135deg,#e8e4de,#b9b2a8 55%,#6e6a66)"></div>
  <div class="work-meta"><span>サイト制作・運営</span><span>A社様</span></div>
</article>
<article class="abs work-card work-2">
  <div class="ph" role="img" aria-label="Photo of a concert crowd under stage lights" style="background:linear-gradient(160deg,#f0c060,#8a4a1a 50%,#1c120c)"></div>
  <div class="work-meta"><span>サイト制作・運営</span><span>B社様</span></div>
</article>

<!-- news -->
<svg class="abs news-blob" width="240" height="270" viewBox="0 0 240 270" aria-hidden="true">
  <path fill="#ffd81a" d="M40 30C100 0 190 10 220 70C245 120 235 200 190 240C140 280 60 265 25 215C-5 170-5 100 10 65C18 50 28 38 40 30Z"/>
</svg>
<div class="abs news-title"><p class="sec-title">NEWS</p><p class="sec-sub">お知らせ</p></div>
<a class="abs news-more pill pill-dark">View more<i></i></a>
<article class="abs news-item news-1"><div class="ph" role="img" aria-label="News thumbnail photo" style="background:linear-gradient(#9fb0c8,#2d3544)"></div><div><p class="news-date">2024.05.12</p><p class="news-txt">新サービスの提供を開始しました。</p></div></article>
<article class="abs news-item news-2"><div class="ph" role="img" aria-label="News thumbnail photo" style="background:linear-gradient(#e7d4a0,#5b4a2a)"></div><div><p class="news-date">2024.04.28</p><p class="news-txt">制作実績を追加しました。</p></div></article>
<article class="abs news-item news-3"><div class="ph" role="img" aria-label="News thumbnail photo" style="background:linear-gradient(#c8c8c8,#3a3a3a)"></div><div><p class="news-date">2024.04.10</p><p class="news-txt">採用情報を更新しました。</p></div></article>
<article class="abs news-item news-4"><div class="ph" role="img" aria-label="News thumbnail photo" style="background:linear-gradient(#b0c4d8,#344050)"></div><div><p class="news-date">2024.03.30</p><p class="news-txt">お知らせ</p></div></article>

<!-- recruit / contact -->
<a class="abs split recruit" role="img" aria-label="Photo of a team meeting, dimmed">
  <p class="split-title">RECRUIT</p><p class="split-sub">採用情報</p>
</a>
<a class="abs split contact" role="img" aria-label="Photo of a city tower at dusk, dimmed">
  <p class="split-title">CONTACT</p><p class="split-sub">お問い合わせ</p>
</a>

<footer class="abs site-footer">
  <div class="logo"><span class="logo-dot"></span>Outlier</div>
  <nav class="nav foot-nav">
    <a href="#">SERVICES</a><a href="#">WORKS</a><a href="#">COMPANY</a><a href="#">NEWS</a><a href="#">RECRUIT</a>
    <a href="#" class="btn-contact">CONTACT</a>
  </nav>
  <p class="copy">© Outlier Inc. All Rights Reserved.</p>
</footer>

</body>
</html>
```